Präsentationsvorlagen für Strahlenschutzkurse
Zielgruppe
Wir bieten Strahlenschutzkurse in der Medizin an. Zielgruppe: Ärztinnen und Ärzte
Stichworte: Erwachsenenbildung, wissenschaftliche Inhalte
Aufgabenstellung
Wir benötigen eine Power-Point Präsentationsvorlage für unsere Kurse.
Auf allen Folien:
*Integration von unserem Logo
*Übernahme unseres bestehenden Farbkonzepts
*Feld für Überschrift
*kleines Textfeld für die Angabe der jeweiligen Quelle
Wir benötigen:
eine Folie nur mit Textfeld (z.B. Aufzählung, kurzer Text)
eine Folie Text mit Bild
eine Folie Bild bzw. Video
eine Folie mit einem wichtigen Lehrinhalt (wichtiger Text) - besondere Vorhebung erwünscht
eine Folie für Anfang bzw. Ende
HEX-CODE:
#4f93fe
#eea62f
#ffffff

```html
<!DOCTYPE html>
<html lang="de">
<head>
<meta charset="utf-8">
<title>Präsentationsvorlage Radiakurs</title>
<link href="https://fonts.googleapis.com/css2?family=Montserrat:ital,wght@0,600;0,700;0,800;1,600&family=Lato:ital,wght@0,400;0,700;1,400;1,700&display=swap" rel="stylesheet">
<style>
:root{
  --navy:#2f5482;
  --blue:#6189c8;
  --orange:#eea62f;
  --green:#8cc63f;
  --white:#ffffff;
  --ink:#2b2b2b;
  --stage:#d7d8da;
  --paper:#f4f4f4;
  --quote:#dfe5f2;
  --photo-a:#6f7f9f;
  --photo-b:#9ba8c2;
}
*{box-sizing:border-box;margin:0;padding:0}
html,body{width:750px;height:1200px;overflow:hidden}
body{background:var(--paper);font-family:"Lato",sans-serif;color:var(--ink);position:relative}
.stage{position:absolute;left:0;top:0;width:750px;height:500px;background:var(--stage)}
.title-slide{position:absolute;left:95px;top:80px;width:560px;height:315px;background:var(--navy);overflow:hidden;box-shadow:0 10px 30px rgba(0,0,0,.18)}
.title-slide .title{position:absolute;left:44px;top:118px;font-family:"Montserrat",sans-serif;font-weight:800;font-size:27px;line-height:1.12;color:var(--white)}
.title-slide .title span{color:var(--blue)}
.title-slide .subtitle{position:absolute;left:44px;top:190px;font-family:"Montserrat",sans-serif;font-weight:600;font-size:10.5px;line-height:1.35;color:var(--white)}
.title-slide .brand{position:absolute;right:34px;top:202px;font-size:13px;color:var(--white)}
.title-slide .band{position:absolute;left:0;right:0;bottom:0;height:52px;background:var(--blue);display:flex;align-items:center;padding-left:44px;font-family:"Montserrat",sans-serif;font-weight:700;font-size:11px;color:var(--white)}

.slide{position:absolute;width:326px;height:183px;background:var(--white);overflow:hidden}
.s1{left:41px;top:551px}.s2{left:386px;top:551px}
.s3{left:41px;top:755px}.s4{left:386px;top:755px}
.s5{left:41px;top:958px}.s6{left:386px;top:958px}

.headline{position:absolute;left:21px;top:14px;font-family:"Montserrat",sans-serif;font-weight:800;font-size:12.5px;color:var(--navy);line-height:15px}
.headline::before{content:"";position:absolute;left:-7px;top:1px;width:2px;height:13px;background:var(--orange)}
.brand{position:absolute;right:22px;top:17px;display:flex;align-items:center;gap:3px;font-family:"Lato",sans-serif;font-weight:700;font-size:5.2px;letter-spacing:.3px;color:var(--navy)}
.brand i{display:block;width:9px;height:9px;border-radius:50%;border:1px solid currentColor}
.brand.light{color:var(--white)}
.body{position:absolute;font-size:3.5px;line-height:6.4px;text-align:justify}
.body p+p{margin-top:5px}
.band{position:absolute;left:0;right:0;bottom:0;height:15px;background:var(--blue)}
.source{position:absolute;left:21px;bottom:5px;font-size:3.8px;font-weight:700;color:var(--white)}
.source.dark{color:var(--blue)}
.pageno{position:absolute;right:12px;bottom:0;width:29px;height:19px;background:var(--orange);color:var(--white);font-family:"Montserrat",sans-serif;font-weight:700;font-size:7px;display:flex;align-items:center;justify-content:center}
.photo{position:absolute;background:linear-gradient(135deg,var(--photo-a),var(--photo-b))}
.photo .cap{position:absolute;left:6px;bottom:6px;font-style:italic;font-weight:700;font-size:8px;line-height:9.5px;color:var(--white)}
.subhead{font-family:"Lato",sans-serif;font-weight:700;font-size:5px;color:var(--blue);margin-bottom:3px}

.s3 .side{position:absolute;left:210px;top:0;width:116px;height:183px;background:var(--blue)}
.s3 .lead{position:absolute;left:21px;top:42px;width:102px;font-style:italic;font-weight:700;font-size:3.6px;line-height:6.3px;color:var(--blue);text-align:justify}
.video{position:absolute;left:139px;top:41px;width:148px;height:110px;background:var(--white);padding:4px;box-shadow:0 2px 6px rgba(0,0,0,.2)}
.video .photo{left:4px;top:4px;right:4px;bottom:4px}
.video svg{position:absolute;left:50%;top:50%;transform:translate(-50%,-50%)}

.steps{position:absolute;left:20px;top:71px;width:290px;display:flex;gap:10px}
.step{flex:1;display:flex;gap:5px}
.step .num{flex:none;width:21px;height:24px;border-radius:50%;background:var(--orange);color:var(--navy);font-size:10px;display:flex;align-items:center;justify-content:center}
.step .txt{font-size:3.5px;line-height:6.3px}
.quote{position:absolute;left:21px;top:135px;width:284px;height:18px;background:var(--quote);padding:4px 8px 0 8px;font-style:italic;font-size:3.3px;line-height:5.6px}
.quote::before{content:"\201C";position:absolute;left:-4px;top:-8px;font-family:"Montserrat",sans-serif;font-weight:800;font-style:italic;font-size:16px;color:var(--navy)}

.s5 .top{position:absolute;left:0;top:0;width:326px;height:87px;background:var(--blue)}
.s5 .headline{color:var(--white)}
.card{position:absolute;left:21px;top:39px;width:284px;height:116px;background:var(--white);box-shadow:0 1px 4px rgba(0,0,0,.12)}
.card svg{position:absolute;left:8px;top:9px}
.card .body{left:147px;top:18px;width:115px}
</style>
</head>
<body>

<section class="stage">
  <div class="title-slide">
    <h1 class="title">Your Presentation<br><span>Title Goes Here</span></h1>
    <p class="subtitle">Lorem ipsum dolor sit amet, consectetur<br>adipiscing elit, sed do eiusmod</p>
    <div class="brand light"><i></i>RADIAKURS</div>
    <div class="band">www.radiakurs-seminare.de</div>
  </div>
</section>

<!-- Text slide -->
<article class="slide s1">
  <h2 class="headline">Your Headline</h2>
  <div class="brand"><i></i>RADIAKURS</div>
  <div class="body" style="left:21px;top:43px;width:284px">
    <p>Lorem ipsum dolor sit amet, consectetur adipiscing elit, sed do eiusmod tempor incididunt ut labore et dolore magna aliqua. Ut enim ad minim veniam, quis nostrud exercitation ullamco laboris nisi ut aliquip ex ea commodo consequat. Duis aute irure dolor in reprehenderit in voluptate velit esse cillum dolore eu fugiat nulla pariatur. Excepteur sint occaecat cupidatat non proident, sunt in culpa qui officia deserunt mollit anim id est laborum.</p>
    <p>Lorem ipsum dolor sit amet, consectetur adipiscing elit, sed do eiusmod tempor incididunt ut labore et dolore magna aliqua. Ut enim ad minim veniam, quis nostrud exercitation ullamco laboris nisi ut aliquip ex ea commodo consequat. Duis aute irure dolor in reprehenderit in voluptate velit esse cillum dolore eu fugiat nulla pariatur. Excepteur sint occaecat cupidatat non proident, sunt in culpa qui officia deserunt mollit anim id est laborum. Lorem ipsum dolor sit amet, consectetur adipiscing elit, sed do eiusmod tempor incididunt ut labore et dolore magna aliqua. Ut enim ad minim veniam, quis nostrud exercitation ullamco laboris nisi ut aliquip ex ea commodo consequat. Duis aute irure dolor in reprehenderit in voluptate velit esse cillum dolore eu fugiat nulla pariatur. Excepteur sint occaecat cupidatat non proident, sunt in culpa qui officia deserunt mollit anim id est laborum.</p>
    <p>Lorem ipsum dolor sit amet, consectetur adipiscing elit, sed do eiusmod tempor incididunt ut labore et dolore magna aliqua. Ut enim ad minim veniam, quis nostrud exercitation ullamco laboris nisi ut aliquip ex ea commodo consequat. Duis aute irure dolor in reprehenderit in voluptate velit esse cillum dolore eu fugiat nulla pariatur. Excepteur sint occaecat cupidatat non proident, sunt in culpa qui officia deserunt mollit anim id est laborum. Lorem ipsum dolor sit amet, consectetur adipiscing elit, sed do eiusmod tempor incididunt ut labore et dolore magna aliqua. Ut enim ad minim veniam, quis nostrud exercitation ullamco laboris nisi ut aliquip ex ea commodo consequat. Duis aute irure dolor in reprehenderit in voluptate velit esse cillum dolore eu fugiat nulla pariatur. Excepteur sint occaecat cupidatat non proident, sunt in culpa qui officia deserunt mollit anim id est laborum.</p>
  </div>
  <div class="band"></div>
  <span class="source">kleines Textfeld für die Angabe der jeweiligen Quelle</span>
  <div class="pageno">01</div>
</article>

<!-- Text with image -->
<article class="slide s2">
  <div class="band"></div>
  <div class="photo" role="img" aria-label="Blau eingefärbtes Foto eines Röntgen-C-Bogens im Untersuchungsraum" style="left:0;top:0;width:128px;height:183px"></div>
  <div class="brand light" style="right:auto;left:20px"><i></i>RADIAKURS</div>
  <h2 class="headline" style="left:147px">Your Headline</h2>
  <div class="body" style="left:147px;top:43px;width:157px">
    <p>Lorem ipsum dolor sit amet, consectetur adipiscing elit, sed do eiusmod tempor incididunt ut labore et dolore magna aliqua. Ut enim ad minim veniam, quis nostrud exercitation ullamco laboris nisi ut aliquip ex ea commodo consequat. Duis aute irure dolor in reprehenderit in voluptate velit esse cillum dolore eu fugiat nulla pariatur. Excepteur sint occaecat cupidatat non proident, sunt in culpa qui officia deserunt mollit anim id est laborum. Lorem ipsum dolor sit amet, consectetur adipiscing elit, sed do eiusmod tempor incididunt ut labore et dolore magna aliqua. Ut enim ad minim veniam, quis nostrud exercitation ullamco laboris nisi ut aliquip ex ea commodo consequat. Duis aute irure dolor in reprehenderit in voluptate velit esse cillum dolore eu fugiat nulla pariatur.</p>
    <p>Lorem ipsum dolor sit amet, consectetur adipiscing elit, sed do eiusmod tempor incididunt ut labore et dolore magna aliqua. Ut enim ad minim veniam, quis nostrud exercitation ullamco laboris nisi ut aliquip ex ea commodo consequat. Duis aute irure dolor in reprehenderit in voluptate velit esse cillum dolore eu fugiat nulla pariatur. Excepteur sint occaecat cupidatat non proident, sunt in culpa qui officia deserunt mollit anim id est laborum. Lorem ipsum dolor sit amet, consectetur adipiscing elit, sed do eiusmod tempor incididunt ut labore et dolore magna aliqua.</p>
  </div>
  <span class="source">kleines Textfeld für die Angabe der jeweiligen Quelle</span>
  <div class="pageno">02</div>
</article>

<!-- Video slide -->
<article class="slide s3">
  <div class="side"></div>
  <h2 class="headline">Your Headline</h2>
  <div class="brand light"><i></i>RADIAKURS</div>
  <p class="lead">Lorem ipsum dolor sit amet, consectetur adipiscing elit, sed do eiusmod tempor incididunt ut labore et dolore magna aliqua. Ut enim ad minim veniam.</p>
  <div class="body" style="left:21px;top:67px;width:102px">
    <p>Lorem ipsum dolor sit amet, consectetur adipiscing elit, sed do eiusmod tempor incididunt ut labore et dolore magna aliqua. Ut enim ad minim veniam, quis nostrud exercitation ullamco laboris nisi ut aliquip ex ea commodo consequat. Duis aute irure dolor in reprehenderit in voluptate velit esse cillum dolore eu fugiat nulla pariatur. Excepteur sint occaecat cupidatat non proident, sunt in culpa qui officia deserunt mollit anim id est laborum. Lorem ipsum dolor sit amet, consectetur adipiscing elit, sed do eiusmod tempor incididunt ut labore et dolore magna aliqua. Ut enim ad minim veniam, quis nostrud exercitation ullamco laboris nisi ut aliquip ex ea commodo consequat. Duis aute irure dolor in reprehenderit in voluptate velit esse.</p>
  </div>
  <div class="video">
    <div class="photo" role="img" aria-label="Videostandbild: Bildschirm mit CT-Aufnahmen und Tastatur"></div>
    <svg width="20" height="20" viewBox="0 0 20 20"><circle cx="10" cy="10" r="8.5" fill="none" stroke="#fff" stroke-width="1.2"/><path d="M8 6 L14.5 10 L8 14 Z" fill="#fff"/></svg>
  </div>
  <span class="source dark">kleines Textfeld für die Angabe der jeweiligen Quelle</span>
  <div class="pageno">03</div>
</article>

<!-- Key teaching content -->
<article class="slide s4">
  <h2 class="headline">Your Headline</h2>
  <div class="brand"><i></i>RADIAKURS</div>
  <div class="body" style="left:21px;top:43px;width:284px">
    <p>Lorem ipsum dolor sit amet, consectetur adipiscing elit, sed do eiusmod tempor incididunt ut labore et dolore magna aliqua. Ut enim ad minim veniam, quis nostrud exercitation ullamco laboris nisi ut aliquip ex ea commodo consequat. Duis aute irure dolor in reprehenderit in voluptate velit esse cillum dolore eu fugiat nulla pariatur. Excepteur sint occaecat cupidatat non proident, sunt in culpa qui officia deserunt mollit anim id est laborum.</p>
  </div>
  <div class="steps">
    <div class="step"><span class="num">1</span><div class="txt"><div class="subhead">Lorem ipsum dolor sit</div>Lorem ipsum dolor sit amet, consectetur adipiscing elit, sed do eiusmod tempor incididunt ut labore et dolore magna aliqua. Ut enim ad minim veniam,</div></div>
    <div class="step"><span class="num">2</span><div class="txt"><div class="subhead">Lorem ipsum dolor sit</div>Lorem ipsum dolor sit amet, consectetur adipiscing elit, sed do eiusmod tempor incididunt ut labore et dolore magna aliqua. Ut enim ad minim veniam,</div></div>
    <div class="step"><span class="num">3</span><div class="txt"><div class="subhead">Lorem ipsum dolor sit</div>Lorem ipsum dolor sit amet, consectetur adipiscing elit, sed do eiusmod tempor incididunt ut labore et dolore magna aliqua. Ut enim ad minim veniam,</div></div>
  </div>
  <p class="quote">Lorem ipsum dolor sit amet, consectetur adipiscing elit, sed do eiusmod tempor incididunt ut labore et dolore magna aliqua. Ut enim ad minim veniam, quis nostrud exercitation ullamco laboris nisi ut aliquip ex ea commodo consequat. Duis aute irure dolor</p>
  <div class="band"></div>
  <span class="source">kleines Textfeld für die Angabe der jeweiligen Quelle</span>
  <div class="pageno">04</div>
</article>

<!-- Chart slide -->
<article class="slide s5">
  <div class="top"></div>
  <h2 class="headline">Your Headline</h2>
  <div class="brand light"><i></i>RADIAKURS</div>
  <div class="card">
    <svg width="128" height="100" viewBox="0 0 128 100" font-family="Lato, sans-serif" font-size="3" fill="#b5b5b5">
      <g stroke="#eeeeee" stroke-width=".4">
        <line x1="12" y1="6" x2="125" y2="6"/><line x1="12" y1="16.5" x2="125" y2="16.5"/><line x1="12" y1="27" x2="125" y2="27"/><line x1="12" y1="37.5" x2="125" y2="37.5"/><line x1="12" y1="48" x2="125" y2="48"/><line x1="12" y1="58.5" x2="125" y2="58.5"/><line x1="12" y1="69" x2="125" y2="69"/><line x1="12" y1="79.5" x2="125" y2="79.5"/><line x1="12" y1="90" x2="125" y2="90"/>
      </g>
      <text x="2" y="7">40</text><text x="2" y="17.5">35</text><text x="2" y="28">30</text><text x="2" y="38.5">25</text><text x="2" y="49">20</text><text x="2" y="59.5">15</text><text x="2" y="70">10</text><text x="3.5" y="80.5">5</text><text x="3.5" y="91">0</text>
      <rect x="32" y="6" width="16" height="84" fill="#2f5482"/>
      <rect x="55" y="16.5" width="16" height="73.5" fill="#eea62f"/>
      <rect x="78" y="32" width="16" height="58" fill="#8cc63f"/>
      <rect x="101" y="22" width="16" height="68" fill="#6189c8"/>
    </svg>
    <div class="body" style="top:16px">
      <div class="subhead">Lorem ipsum dolor sit</div>
      <p>Lorem ipsum dolor sit amet, consectetur adipiscing elit, sed do eiusmod tempor incididunt ut labore et dolore magna aliqua. Ut enim ad minim veniam, quis nostrud exercitation ullamco laboris nisi ut aliquip ex ea commodo consequat. Duis aute irure dolor in reprehenderit in voluptate velit esse cillum dolore eu fugiat nulla pariatur. Excepteur sint occaecat cupidatat non proident, sunt in culpa qui officia deserunt mollit anim id est laborum. Lorem ipsum dolor sit amet, consectetur adipiscing elit, sed do eiusmod tempor incididunt ut labore et dolore magna aliqua. Ut enim ad minim veniam, quis nostrud exercitation ullamco laboris nisi ut aliquip ex ea commodo consequat. Duis aute irure dolor in reprehenderit in voluptate velit esse cillum dolore eu fugiat nulla pariatur.</p>
    </div>
  </div>
  <div class="band"></div>
  <span class="source">kleines Textfeld für die Angabe der jeweiligen Quelle</span>
  <div class="pageno">05</div>
</article>

<!-- Two images -->
<article class="slide s6">
  <h2 class="headline">Your Headline</h2>
  <div class="brand"><i></i>RADIAKURS</div>
  <div class="photo" role="img" aria-label="Blau eingefärbtes Foto eines Röntgen-C-Bogens in Nahaufnahme" style="left:26px;top:46px;width:123px;height:69px"><span class="cap">Lorem ipsum<br>dolor sit amet</span></div>
  <div class="photo" role="img" aria-label="Blau eingefärbtes Foto eines Röntgen-C-Bogens in Nahaufnahme" style="left:174px;top:46px;width:124px;height:69px"><span class="cap">Lorem ipsum<br>dolor sit amet</span></div>
  <div class="body" style="left:31px;top:122px;width:113px"><p>Lorem ipsum dolor sit amet, consectetur adipiscing elit, sed do eiusmod tempor incididunt ut labore et dolore magna aliqua. Ut enim ad minim veniam, quis nostrud exercitation ullamco laboris nisi ut aliquip ex ea commodo consequat.</p></div>
  <div class="body" style="left:179px;top:122px;width:113px"><p>Lorem ipsum dolor sit amet, consectetur adipiscing elit, sed do eiusmod tempor incididunt ut labore et dolore magna aliqua. Ut enim ad minim veniam, quis nostrud exercitation ullamco laboris nisi ut aliquip ex ea commodo consequat.</p></div>
  <div class="band"></div>
  <span class="source">kleines Textfeld für die Angabe der jeweiligen Quelle</span>
  <div class="pageno">04</div>
</article>

</body>
</html>
```